Consulting, Investors, Joint Venture Website

Founded in April 2018, Marendo Advisers Limited (MAL) is an advisory consulting firm specializing in engaging investors in business ventures in Tanzania.
With extensive experience in construction, energy, oil and gas and the legal professions, our team assembles our expertise that allows foreign investors to set foot and flourish in the Tanzanian market.
MAL is locally owned, founded and registered. Our shareholders are cultured Tanzanian citizens with extensive corporate experience in South Africa, Tanzania, United Kingdom and the United States.

Our mission is to provide responsive and unrivalled professional advice from learned and experienced professionals versed in the local market, with an understanding of the cultural and logistical challenges faced by foreign investors.

Our vision is to provide a complete investor’s package that initiates with company registration, compliance and documentation services and ultimately operational facilitation services.

Target Market(s)

Foreign Investors, International companies

Industry/Entity Type

Business Consultant

Number of Pages Required

5+ page

Requirements
Must have
• It will be 5 pages - Home, About Us, Services, Portfolio, Contact Us
Nice to have
• if it can look like https://www.vq-sample.com/
• or https://www.torvell.com or http://www.bramwickpoint.com/

```html
<!DOCTYPE html>
<html lang="en">
<head>
<meta charset="utf-8">
<title>Marendo Advisers</title>
<link href="https://fonts.googleapis.com/css2?family=Montserrat:wght@500;600;700&family=Open+Sans:wght@400;600;700&family=Raleway:wght@300;400&display=swap" rel="stylesheet">
<style>
:root{
  --blue:#1258a8;
  --blue-dark:#0e4d96;
  --orange:#f5941e;
  --ink:#222;
  --muted:#666;
  --panel-gray:#5e5e5e;
  --light:#f1f1f1;
  --white:#fff;
}
*{box-sizing:border-box;margin:0;padding:0}
html,body{width:1200px;height:2163px;overflow:hidden}
body{background:#f7f7f7;font-family:"Open Sans",Arial,sans-serif;color:var(--ink);position:relative}
.backdrop-band{position:absolute;left:0;top:0;width:1200px;height:539px;background:var(--blue)}
.page{position:absolute;left:124px;top:81px;width:953px;height:1856px;background:var(--white);box-shadow:0 40px 80px rgba(0,0,0,.18);overflow:hidden}
.abs{position:absolute}

/* hero */
.hero{left:0;top:0;width:953px;height:458px;background:linear-gradient(100deg,#e9ece9 0%,#d6d9da 35%,#bfc3c6 60%,#e5e6e6 100%)}
.hero-shape{left:0;top:0}
.brand{left:120px;top:46px;display:flex;align-items:center;gap:8px;font-family:"Montserrat",sans-serif;font-weight:700;font-size:22px;color:var(--blue);letter-spacing:.5px}
.brand-mark{width:30px;height:30px;background:var(--blue)}
.nav{left:433px;top:54px;display:flex;gap:20px;align-items:center;font-family:"Montserrat",sans-serif;font-size:10px;font-weight:500;color:#222}
.nav .events{background:var(--orange);color:#fff;border-radius:14px;padding:6px 20px;margin-left:8px}
.hero-title{left:196px;top:152px;font-family:"Raleway",sans-serif;font-weight:400;font-size:20px;line-height:25px;color:#222;border-left:2px solid var(--blue);padding-left:14px;margin-left:-16px}
.hero-link{left:200px;top:237px;font-size:11px;color:var(--orange)}
.offer{top:339px;width:296px;height:164px;background:#fff;box-shadow:0 4px 14px rgba(0,0,0,.12);text-align:center;padding:24px 22px 0}
.offer h3{font-family:"Montserrat",sans-serif;font-size:11px;font-weight:700;line-height:14px;color:var(--blue)}
.offer.alt h3{color:var(--orange)}
.offer p{font-size:10px;line-height:13px;margin-top:10px;color:#222}
.pill{display:inline-block;margin-top:14px;padding:5px 14px;border-radius:14px;font-size:10px;color:#fff;background:var(--blue)}
.offer.alt .pill{background:var(--orange)}

/* services strip */
.services{left:120px;top:535px;width:712px;height:275px}
.service{position:absolute;top:140px;color:#fff;font-family:"Montserrat",sans-serif}
.service h4{font-size:12px;font-weight:700;line-height:15px}
.service p{font-size:8px;line-height:11px;margin-top:4px;opacity:.85}
.service span{display:inline-block;margin-top:24px;font-size:8px;background:rgba(255,255,255,.15);padding:3px 12px}

/* next move */
.next{left:0;top:834px;width:953px;height:248px;background:linear-gradient(90deg,#e4e4e4,#ededed 40%,#f0f0f0)}
.next-photo{left:78px;top:0;width:300px;height:248px;background:linear-gradient(180deg,#d9d4cf,#c6c2bf)}
.next-copy{left:489px;top:56px;width:310px}
.next-copy h2{font-family:"Montserrat",sans-serif;font-size:16px;font-weight:600;color:#111}
.next-copy p{font-size:9.5px;line-height:13px;margin-top:14px;color:#333}
.btn-row{display:flex;gap:6px;margin-top:14px}
.btn{font-family:"Montserrat",sans-serif;font-size:7.5px;font-weight:600;padding:7px 12px;text-transform:uppercase}
.btn.light{background:#fff;color:#333}
.btn.solid{background:var(--orange);color:#fff}

/* case studies */
.case{top:1142px;width:234px;height:309px;background:#fff;box-shadow:0 4px 14px rgba(0,0,0,.09);text-align:center}
.case-img{height:130px}
.case h5{font-size:13px;font-weight:600;color:#333;margin-top:26px}
.case p{font-size:10px;line-height:16px;color:#777;padding:6px 26px 0}
.case .read{display:inline-block;margin-top:14px;background:var(--orange);color:#fff;font-family:"Montserrat",sans-serif;font-size:8px;font-weight:700;padding:6px 17px}

/* footer */
.footer{left:0;top:1513px;width:953px;height:265px;background:var(--blue);color:#fff}
.footer .brand{left:137px;top:70px;color:#fff;font-size:20px}
.footer .brand-mark{background:#fff;width:26px;height:26px}
.foot-about{left:137px;top:126px;width:185px;font-size:8.5px;line-height:13px}
.foot-col{top:97px;font-size:8.5px;line-height:14px}
.foot-col h6{font-size:11px;font-weight:400;margin-bottom:16px}
.foot-col li{list-style:none;margin-bottom:10px}
.foot-col .strong{font-weight:700}
.sub-input{width:155px;height:19px;background:#fff;color:#333;font-size:8px;padding:4px 8px 0 30px;margin-top:10px;position:relative}
.sub-input svg{position:absolute;left:10px;top:5px}
.sub-btn{display:inline-block;margin-top:8px;background:var(--orange);font-size:8px;padding:4px 18px}
.bottom-bar{left:0;top:1778px;width:953px;height:78px;background:var(--blue-dark);color:#fff}
.bottom-bar small{position:absolute;left:137px;top:34px;font-size:8px}
.socials{position:absolute;left:666px;top:32px;display:flex;gap:9px}
.socials i{width:15px;height:15px;border:1px solid #fff;border-radius:50%}
</style>
</head>
<body>
<div class="backdrop-band"></div>
<main class="page">
  <section class="abs hero" role="img" aria-label="Photo of two colleagues reviewing work at a laptop in a bright office with a potted plant"></section>
  <svg class="abs hero-shape" width="953" height="458" viewBox="0 0 953 458">
    <polygon points="600,458 953,178 953,190 615,458" fill="#fff"/>
    <polygon points="628,458 953,200 953,458" fill="var(--orange)"/>
  </svg>
  <div class="abs brand"><span class="brand-mark"></span>Marendo Advisers</div>
  <nav class="abs nav">
    <span>HOME</span><span>ABOUT US</span><span>SERVICES</span><span>PORTFOLIO</span><span>CONTACT US</span><span class="events">EVENTS</span>
  </nav>
  <h1 class="abs hero-title">Tanzania most trusted<br>platform for Investing<br>&amp; advisory consulting</h1>
  <a class="abs hero-link">Our Services</a>

  <article class="abs offer" style="left:177px">
    <h3>COMPLETE INVESTOR'S PACKAGE IN<br>TANZANIA MOST PROMISING STARTUPS</h3>
    <p>Diversify your investment portfolio with access to highly curated and personalised deal flow from Tanzania and beyond</p>
    <span class="pill">I am Investor</span>
  </article>
  <article class="abs offer alt" style="left:480px">
    <h3>COMPLETE I ADVISORY<br>CONSULTING FIRM SPECIALIZING</h3>
    <p>Diversify your investment portfolio with access to highly curated and personalised deal flow from Tanzania and beyond</p>
    <span class="pill">Need Consulting</span>
  </article>

  <section class="abs services">
    <svg width="712" height="275" viewBox="0 0 712 275" role="img" aria-label="Four slanted service panels over photos of teams at work">
      <polygon points="0,0 232,0 128,275 0,275" fill="#6a6a6a"/>
      <polygon points="232,0 411,0 310,275 128,275" fill="#2a62ad"/>
      <polygon points="411,0 591,0 484,275 310,275" fill="#f0a23a"/>
      <polygon points="591,0 712,0 712,275 484,275" fill="#626262"/>
      <polygon points="226,0 238,0 134,275 122,275" fill="#fff"/>
      <polygon points="405,0 417,0 316,275 304,275" fill="#fff"/>
      <polygon points="585,0 597,0 490,275 478,275" fill="#fff"/>
    </svg>
    <div class="service" style="left:29px"><h4>STRATEGY<br>CONSULTING</h4><p>MAPPING YOUR<br>JOURNEY</p><span>Read More</span></div>
    <div class="service" style="left:192px"><h4>CHANGE<br>MANAGEMENT</h4><p>BUILDING SUSTAINABILITY<br>FROM DAY ONE</p><span>Read More</span></div>
    <div class="service" style="left:376px"><h4>PROGRAMME<br>MANAGEMENT</h4><p>CREATING THE<br>EXECUTION VEHICLE</p><span>Read More</span></div>
    <div class="service" style="left:563px"><h4>ORGANISATIONAL<br>DESIGN</h4><p>SEEING CHALLENGES IN<br>A NEW LIGHT</p><span>Read More</span></div>
  </section>

  <section class="abs next">
    <div class="abs next-photo" role="img" aria-label="Photo of a young businessman in a white shirt and tie looking sideways"></div>
    <div class="abs next-copy">
      <h2>YOUR NEXT MOVE</h2>
      <p>The future is yours to build, today. To build the future requires rethinking how you plan and strategize in your organization. Our insights equip you to predict and adapt to emerging trends including artificial intelligence, digital, and ways of working—all while instilling a fundamental commitment to people.</p>
      <div class="btn-row"><span class="btn light">Learn More</span><span class="btn solid">Your Next Move</span></div>
    </div>
  </section>

  <article class="abs case" style="left:118px">
    <div class="case-img" role="img" aria-label="Photo of a hand holding a rising bar chart in an office" style="background:linear-gradient(135deg,#e8eef3,#b9cbd9)"></div>
    <h5>Case Study</h5>
    <p>Contrary to popular belief, Lorem Ipsum is not simply random text. It has roots in a piece of classical Latin.</p>
    <span class="read">READ MORE</span>
  </article>
  <article class="abs case" style="left:358px">
    <div class="case-img" role="img" aria-label="Photo of a team stacking hands together" style="background:linear-gradient(135deg,#e07a3a,#3d6f8f)"></div>
    <h5>Case Study</h5>
    <p>Contrary to popular belief, Lorem Ipsum is not simply random text. It has roots in a piece of classical Latin.</p>
    <span class="read">READ MORE</span>
  </article>
  <article class="abs case" style="left:598px">
    <div class="case-img" role="img" aria-label="Photo of two silhouetted people shaking hands by a bright window" style="background:linear-gradient(90deg,#2f2b28,#d9c9a6 55%,#3a3530)"></div>
    <h5>Case Study</h5>
    <p>Contrary to popular belief, Lorem Ipsum is not simply random text. It has roots in a piece of classical Latin.</p>
    <span class="read">READ MORE</span>
  </article>

  <footer class="abs footer">
    <div class="abs brand"><span class="brand-mark"></span>Marendo Advisers</div>
    <p class="abs foot-about">Worth never leaves the hands of its customers after the pre-eminent procedure of finances. It includes both secured and unsecured loans. Security involves a form of collateral as an assurance the loan will be repaid. It means issuing additional shares of common stock to an investor.</p>
    <div class="abs foot-col" style="left:384px;width:130px">
      <h6>Conact us</h6>
      <p>14 Kilwa Lane, Msasani Peninsula, Dar es Salaam 14111</p>
      <p class="strong" style="margin-top:6px">0700 41 5520</p>
      <p class="strong" style="margin-top:6px">hello@marendoadvisers.co</p>
    </div>
    <ul class="abs foot-col" style="left:560px">
      <h6>Discover</h6>
      <li>About Us</li><li>Our Work</li><li>Services</li><li>Our Team</li>
    </ul>
    <div class="abs foot-col" style="left:659px;width:170px">
      <h6>Subscribe with us</h6>
      <p style="line-height:11px">Sign up for our mailing list to get latest updates and offers</p>
      <div class="sub-input"><svg width="12" height="9" viewBox="0 0 12 9"><rect x=".5" y=".5" width="11" height="8" fill="none" stroke="#f5941e"/><path d="M.5 .5 6 5l5.5-4.5" fill="none" stroke="#f5941e"/></svg>Email Address</div>
      <span class="sub-btn">Submit</span>
    </div>
  </footer>
  <div class="abs bottom-bar">
    <small>(c) powered by Harbourline Studio Developed by Pinecrest Labs</small>
    <div class="socials"><i></i><i></i><i></i><i></i></div>
  </div>
</main>
</body>
</html>
```